Infographic Template that Showcases individual wine producers of the World

Needs to be an infographic template A4 size. Allowing Winemaker introduction, Location (with Map) Climate, Soils, Winemaking methods, and Varietals Grown. This template will be applied to wines we focus as a part of our restaurant wine experience. Colour Focus should be red, white and black. An example of some italian wine makers is shown in the images. Though I would prefer that it is not black background but essentially has these sections and is clean with the ability to add specific text, images and maps.

Target Market(s)

Our Guests at the restaurant as a take away during a wine experience event

Industry/Entity Type

Hospitality

Font styles to use
Sans Serif

Colors
EB3D1F
EC4F4E
F09395
F8D3D4
FCEDEE

Requirements
Must have
• Must be a templaate so we can add winegrowers details when we offer the wine
Nice to have
• Nice for the infographic design to be unique, carry our logo, attached and be clean lines and print well on A4 or greater

```html
<!DOCTYPE html>
<html lang="en">
<head>
<meta charset="utf-8">
<title>Wine Producer Infographic</title>
<link href="https://fonts.googleapis.com/css2?family=Bebas+Neue&display=swap" rel="stylesheet">
<style>
  :root {
    --navy: #272b3d;
    --crimson: #e52b4d;
    --red: #ec4f4e;
    --rose: #f09395;
    --blush: #f8d3d4;
    --mist: #fcedee;
    --white: #ffffff;
    --ink: #2b2b2b;
  }
  * { margin: 0; padding: 0; box-sizing: border-box; }
  html, body { width: 849px; height: 1200px; overflow: hidden; background: var(--white); }
  body { font-family: "Bebas Neue", "Oswald", sans-serif; color: var(--ink); }
  .sheet { position: relative; width: 849px; height: 1200px; overflow: hidden; background: var(--white); }

  .brand-bar { position: absolute; left: 0; top: 0; width: 849px; height: 140px; background: var(--navy);
    display: flex; align-items: center; justify-content: center; gap: 16px; }
  .brand-mark { width: 44px; height: 44px; border-radius: 50%; border: 2px solid var(--white); }
  .brand-name { color: var(--white); font-size: 46px; letter-spacing: 5px; line-height: .85; }
  .brand-name small { display: block; font-size: 20px; letter-spacing: 4px; text-align: center; }

  .hero { position: absolute; left: 0; top: 0; width: 849px; height: 480px; }
  .intro { position: absolute; left: 56px; top: 172px; width: 360px; color: var(--white); }
  .section-title { font-size: 44px; letter-spacing: 1px; line-height: 1; }
  .intro .section-title { margin-bottom: 16px; }
  .intro p { font-size: 20px; line-height: 1.12; letter-spacing: .5px; }

  .varietals { position: absolute; left: 452px; top: 152px; width: 360px; height: 222px; background: var(--white);
    border-radius: 14px; padding: 18px 22px; text-align: center; }
  .varietals .section-title { color: var(--crimson); font-size: 34px; }
  .varietals .lead { font-size: 14px; letter-spacing: 1px; color: var(--ink); }
  .glass-row { display: flex; justify-content: space-between; margin-top: 16px; padding: 0 6px; }
  .glass { width: 66px; text-align: center; font-size: 15px; line-height: 1; color: var(--ink); }
  .glass-art { width: 40px; height: 86px; margin: 0 auto 8px; border-radius: 20px 20px 6px 6px;
    background: linear-gradient(to bottom, var(--mist) 0 40%, var(--tone) 40% 62%, #d9d9d9 62%); }

  .climate { position: absolute; left: 0; top: 420px; width: 849px; height: 180px; }
  .climate-title { position: absolute; left: 96px; top: 18px; color: var(--crimson); font-size: 42px; }
  .climate-art { position: absolute; left: 52px; top: 72px; width: 46px; height: 60px; border-radius: 22px 22px 4px 4px;
    background: linear-gradient(var(--rose), var(--crimson)); }
  .climate-range { position: absolute; left: 112px; top: 70px; color: var(--crimson); font-size: 64px; letter-spacing: 1px; }
  .climate-text { position: absolute; left: 452px; top: 40px; width: 360px; color: var(--crimson); font-size: 22px; line-height: 1.1; }

  .soils { position: absolute; left: 40px; top: 602px; width: 360px; }
  .soils .section-title { color: var(--crimson); font-size: 42px; margin-bottom: 22px; }
  .soil-row { display: flex; gap: 22px; }
  .soil { width: 64px; text-align: center; font-size: 14px; line-height: 1; color: #8a8a8a; }
  .soil-art { width: 64px; height: 34px; border-radius: 32px 32px 4px 4px; margin-bottom: 8px; }

  .location { position: absolute; left: 420px; top: 596px; width: 429px; height: 170px; background: var(--crimson); color: var(--white); }
  .location .section-title { position: absolute; left: 30px; top: 6px; font-size: 42px; }
  .location-name { position: absolute; left: 30px; top: 56px; font-size: 26px; line-height: 1; }
  .location-name small { display: block; font-size: 18px; }
  .location-notes { position: absolute; left: 30px; top: 104px; width: 190px; font-size: 11px; line-height: 1.05; letter-spacing: .3px; }
  .map { position: absolute; left: 262px; top: 30px; width: 110px; height: 110px; background: var(--blush); border-radius: 30% 45% 35% 50%; }

  .methods-title { position: absolute; left: 0; top: 768px; width: 849px; text-align: center; color: var(--crimson); font-size: 40px; }
  .methods { position: absolute; left: 44px; top: 820px; width: 770px; display: grid; grid-template-columns: repeat(4, 1fr); }
  .method { padding: 0 18px 0 12px; border-left: 1px solid var(--rose); }
  .method:first-child { border-left: none; padding-left: 0; }
  .method h3 { font-weight: 400; color: var(--crimson); font-size: 30px; margin-bottom: 6px; }
  .method p { color: var(--crimson); font-size: 19px; line-height: 1.1; }

  .footer { position: absolute; left: 0; top: 1130px; width: 849px; height: 70px; background: var(--navy);
    display: flex; align-items: center; justify-content: center; gap: 12px; }
  .footer .brand-mark { width: 30px; height: 30px; }
  .footer .brand-name { font-size: 30px; letter-spacing: 3px; }
  .footer .brand-name small { font-size: 14px; letter-spacing: 3px; }
</style>
</head>
<body>
<div class="sheet">

  <svg class="hero" viewBox="0 0 849 480" aria-hidden="true">
    <path d="M0 130 H849 V380 C780 380 760 410 690 405 C620 400 610 375 540 380 C470 385 450 410 380 405 C300 400 280 370 200 385 C130 398 90 420 0 400 Z" fill="var(--crimson)"/>
    <path d="M0 610 L560 450 L849 530 V600 L0 680 Z" fill="var(--mist)"/>
    <path d="M0 1060 C200 1020 380 1100 560 1060 C700 1030 790 1050 849 1040 V1130 H0 Z" fill="var(--mist)"/>
  </svg>
  <svg style="position:absolute;left:0;top:430px" width="849" height="250" aria-hidden="true">
    <path d="M0 200 L560 40 L849 110 V170 L0 250 Z" fill="var(--mist)"/>
  </svg>
  <svg style="position:absolute;left:0;top:1000px" width="849" height="130" aria-hidden="true">
    <path d="M0 70 C200 30 380 110 560 70 C700 40 790 60 849 50 V130 H0 Z" fill="var(--mist)"/>
  </svg>

  <header class="brand-bar">
    <span class="brand-mark"></span>
    <div class="brand-name">EMBERLY<small>KITCHEN &amp; BAR</small></div>
  </header>

  <section class="intro">
    <h2 class="section-title">Introduction</h2>
    <p>Lorem ipsum dolor sit amet, consectetuer adipiscing elit, sed diam nonummy nibh euismod tincidunt ut laoreet dolore magna aliquam erat volutpat. Ut wisi adipiscing elit, sed diam nonummy nibh euismod tincidunt ut laoreet dolore magna aliquam erat volutpat. Ut wisi</p>
  </section>

  <section class="varietals">
    <h2 class="section-title">Varitals Grown</h2>
    <p class="lead">We have many varities like</p>
    <div class="glass-row">
      <div class="glass"><div class="glass-art" role="img" aria-label="Glass of rich white wine" style="--tone:#f3e7a0"></div>Rich<br>White</div>
      <div class="glass"><div class="glass-art" role="img" aria-label="Glass of bold red wine" style="--tone:#8e1b2c"></div>Bold<br>Red</div>
      <div class="glass"><div class="glass-art" role="img" aria-label="Glass of light red wine" style="--tone:#c53a4c"></div>Light<br>Red</div>
      <div class="glass"><div class="glass-art" role="img" aria-label="Glass of dessert wine" style="--tone:#7d1a33"></div>Dessert</div>
    </div>
  </section>

  <section class="climate">
    <h2 class="climate-title">Climate</h2>
    <div class="climate-art" role="img" aria-label="Tree illustration"></div>
    <p class="climate-range">30° - 40° C</p>
    <p class="climate-text">" Area to write about Climate " Lorem ipsum dolor sit amet, consectetuer adipiscing elit, sed diam nonummy nibh euismod tincidunt ut laoreet dolore magna aliquam erat volutpat.</p>
  </section>

  <section class="soils">
    <h2 class="section-title">Soils</h2>
    <div class="soil-row">
      <div class="soil"><div class="soil-art" role="img" aria-label="Sandy soil sample" style="background:#cdb89a"></div>Sandy<br>Soil</div>
      <div class="soil"><div class="soil-art" role="img" aria-label="Silt soil sample" style="background:#8b7a72"></div>Silt<br>Soil</div>
      <div class="soil"><div class="soil-art" role="img" aria-label="Clay soil sample" style="background:#a9a3a0"></div>Clay<br>Soil</div>
      <div class="soil"><div class="soil-art" role="img" aria-label="Loamy soil sample" style="background:#2e2e2e"></div>Loamy<br>Soil</div>
    </div>
  </section>

  <section class="location">
    <h2 class="section-title">Location</h2>
    <p class="location-name">Location Name<small>Dimensions</small></p>
    <p class="location-notes">Lorem ipsum dolor sit amet, consectetuer adipiscing elit, sed diam nonummy nibh euismod tincidunt ut laoreet dolore magna aliquam erat volutpat. Ut wisi enim ad minim veniam, quis nostrud exerci tation.</p>
    <div class="map" role="img" aria-label="Map of the winery region"></div>
  </section>

  <h2 class="methods-title">Wine Making Methods</h2>
  <section class="methods">
    <article class="method"><h3>Method 1</h3><p>Lorem ipsum dolor sit amet, consectetuer adipiscing elit, sed diam nonummy nibh euismod tincidunt</p></article>
    <article class="method"><h3>Method 2</h3><p>Lorem ipsum dolor sit amet, consectetuer adipiscing elit, sed diam nonummy nibh euismod tincidunt</p></article>
    <article class="method"><h3>Method 3</h3><p>Lorem ipsum dolor sit amet, consectetuer adipiscing elit, sed diam nonummy nibh euismod tincidunt</p></article>
    <article class="method"><h3>Method 4</h3><p>Lorem ipsum dolor sit amet, consectetuer adipiscing elit, sed diam nonummy nibh euismod tincidunt</p></article>
  </section>

  <footer class="footer">
    <span class="brand-mark"></span>
    <div class="brand-name">EMBERLY<small>KITCHEN &amp; BAR</small></div>
  </footer>

</div>
</body>
</html>
```